Harbor Finwave Club Post Card

Looking for an original Eye Catching Post Card. This is for a Swim Club. We offer Swim Programs for age 4+

Highest Quality Coached Program

Small Team Provincial Champions

I want it to help fill my swim programs I offer Fitness Programs, Competitive and Swim Academy. Development swimmers to High Performance athletes.
I will attach a previous one i had done, but I want a really Eye Catching one - Double sided with information on one side as well. Or contact information.

"Harbor Finwave Club is a Coach Run Swim Club, bringing Passion & Uniqueness to our Athlete Centered Programs"

Target Market(s)

New Families to the Sport of Swimming

Industry/Entity Type

Club

Colors
3176b5
0355a3

Requirements
Must have
• Logo and My Own kids in the pictures not fab ones
Nice to have
• "Harbor Finwave Club is a Coach Run Swim Club, bringing Passion & Uniqueness to our Athlete Centered Programs"
Should not have
• Should not look like my original one at all

```html
<!DOCTYPE html>
<html lang="en">
<head>
<meta charset="utf-8">
<title>Harbor Finwave Club Post Card</title>
<link href="https://fonts.googleapis.com/css2?family=Kalam:wght@400;700&family=Roboto:wght@400;500;700&family=Ubuntu:wght@700&display=swap" rel="stylesheet">
<style>
  :root {
    --navy: #26237a;
    --navy-deep: #1b1860;
    --blue: #0355a3;
    --blue-light: #3176b5;
    --sky: #1c8ad6;
    --silver: #d3d6dd;
    --silver-dark: #9ea3ad;
    --paper: #f3f4f6;
    --ink: #1d1a22;
    --orange: #f0692a;
    --white: #ffffff;
    --backdrop: #e6e8ec;
  }
  html, body {
    margin: 0;
    padding: 0;
    width: 1035px;
    height: 1200px;
    overflow: hidden;
    background: var(--backdrop);
  }
  .canvas {
    width: 1035px;
    height: 1200px;
    display: flex;
    flex-direction: column;
    align-items: center;
    gap: 20px;
    padding-top: 30px;
    box-sizing: border-box;
  }
  .postcard {
    width: 840px;
    height: 560px;
    box-shadow: 0 6px 18px rgba(20, 24, 40, 0.25);
  }
  .postcard svg { display: block; }
  .quote { font-family: "Kalam", cursive; fill: var(--white); }
  .quote-mark { fill: var(--orange); font-weight: 700; }
  .club-name { font-family: "Ubuntu", sans-serif; font-weight: 700; letter-spacing: 1px; }
  .club-name--light { fill: var(--white); }
  .club-name--dark { fill: var(--ink); }
  .contact { font-family: "Roboto", sans-serif; fill: var(--white); }
  .contact-phone { font-weight: 700; }
  .contact-line { font-weight: 500; }
  .ribbon-text { font-family: "Roboto", sans-serif; font-weight: 700; font-size: 12px; fill: var(--white); }
  .program-list { font-family: "Roboto", sans-serif; font-size: 12.5px; fill: var(--white); }
  .bullet { fill: var(--sky); }
  .icon-light { fill: var(--white); }
  .icon-accent { fill: var(--orange); }
  .stop-navy { stop-color: var(--navy); }
  .stop-navy-deep { stop-color: var(--navy-deep); }
  .stop-blue { stop-color: var(--blue); }
  .stop-sky { stop-color: var(--sky); }
  .stop-silver { stop-color: var(--silver); }
  .stop-silver-dark { stop-color: var(--silver-dark); }
  .stop-white { stop-color: var(--white); }
</style>
</head>
<body>
<main class="canvas">

  <!-- Front side -->
  <section class="postcard postcard--front">
    <svg width="840" height="560" viewBox="0 0 840 560">
      <defs>
        <linearGradient id="front-blue" x1="0" y1="0" x2="1" y2="1">
          <stop offset="0" class="stop-sky"/>
          <stop offset="0.6" class="stop-blue"/>
          <stop offset="1" class="stop-navy"/>
        </linearGradient>
        <linearGradient id="front-silver" x1="0" y1="0" x2="1" y2="0">
          <stop offset="0" class="stop-white"/>
          <stop offset="1" class="stop-silver-dark"/>
        </linearGradient>
        <linearGradient id="photo-team" x1="0" y1="0" x2="0" y2="1">
          <stop offset="0" stop-color="#6f8fb3"/>
          <stop offset="1" stop-color="#2f3f74"/>
        </linearGradient>
        <linearGradient id="photo-girls" x1="0" y1="0" x2="1" y2="1">
          <stop offset="0" stop-color="#5fa8d8"/>
          <stop offset="1" stop-color="#1f2a6e"/>
        </linearGradient>
        <symbol id="icon-phone" viewBox="0 0 24 24">
          <path d="M6.6 10.8c1.4 2.8 3.8 5.1 6.6 6.6l2.2-2.2c.3-.3.7-.4 1-.2 1.1.4 2.3.6 3.6.6.6 0 1 .4 1 1V20c0 .6-.4 1-1 1C10.6 21 3 13.4 3 4c0-.6.4-1 1-1h3.5c.6 0 1 .4 1 1 0 1.3.2 2.5.6 3.6.1.3 0 .7-.2 1L6.6 10.8z"/>
        </symbol>
        <symbol id="icon-mail" viewBox="0 0 24 24">
          <path d="M2 5h20v14H2z M2 5l10 8 10-8" fill="none" stroke="currentColor" stroke-width="0"/>
          <path d="M2 5h20v2l-10 7L2 7z"/>
          <path d="M2 9l10 7 10-7v10H2z"/>
        </symbol>
        <symbol id="icon-globe" viewBox="0 0 24 24">
          <circle cx="12" cy="12" r="9" fill="none" stroke="currentColor" stroke-width="2"/>
          <ellipse cx="12" cy="12" rx="4" ry="9" fill="none" stroke="currentColor" stroke-width="1.6"/>
          <path d="M3 12h18M5 7.5h14M5 16.5h14" stroke="currentColor" stroke-width="1.4"/>
        </symbol>
      </defs>

      <rect class="front-band" width="840" height="560" fill="var(--navy)"/>

      <rect class="photo photo--team" x="470" y="0" width="370" height="262" fill="url(#photo-team)"
            role="img" aria-label="Photo of young club swimmers in caps and goggles at a pool deck"/>
      <rect class="photo photo--girls" x="470" y="252" width="370" height="308" fill="url(#photo-girls)"
            role="img" aria-label="Photo of smiling club swimmers in team jackets"/>
      <path class="photo-divider" d="M600 262 C670 236 760 226 840 236" fill="none" stroke="var(--white)" stroke-width="10"/>

      <circle class="front-ring" cx="250" cy="620" r="510" fill="url(#front-silver)"/>
      <circle class="front-disc" cx="250" cy="620" r="490" fill="url(#front-blue)"/>

      <text class="quote" text-anchor="middle" font-size="15">
        <tspan x="262" y="28"><tspan class="quote-mark">❝</tspan> We teach leadership</tspan>
        <tspan x="262" y="46">we are part of the community</tspan>
        <tspan x="262" y="66" font-size="17">we build Friendships that last a lifetime</tspan>
        <tspan x="262" y="84">We teach Kids to</tspan>
        <tspan x="262" y="104" font-size="17">Swim and LOVE the Water<tspan class="quote-mark">❞</tspan></tspan>
      </text>

      <g class="club-mark">
        <circle cx="100" cy="242" r="30" fill="var(--white)"/>
        <text class="club-name club-name--light" font-size="24">
          <tspan x="148" y="218">HARBOR</tspan>
          <tspan x="148" y="246">FINWAVE</tspan>
          <tspan x="148" y="274">CLUB</tspan>
        </text>
      </g>

      <g class="contact-block">
        <use href="#icon-phone" x="62" y="323" width="26" height="26" class="icon-light"/>
        <text class="contact contact-phone" x="96" y="346" font-size="29">780-555-0147</text>
        <use href="#icon-mail" x="62" y="372" width="20" height="20" class="icon-light"/>
        <text class="contact contact-line" x="94" y="389" font-size="17">coach@finwaveclub.com</text>
        <use href="#icon-globe" x="62" y="407" width="20" height="20" class="icon-light" color="var(--white)"/>
        <text class="contact contact-line" x="94" y="423" font-size="17">www.finwaveclub.com</text>
      </g>
    </svg>
  </section>

  <!-- Back side -->
  <section class="postcard postcard--back">
    <svg width="840" height="560" viewBox="0 0 840 560">
      <defs>
        <linearGradient id="back-navy" x1="0" y1="0" x2="0" y2="1">
          <stop offset="0" class="stop-navy"/>
          <stop offset="1" class="stop-navy-deep"/>
        </linearGradient>
        <linearGradient id="back-paper" x1="0" y1="0" x2="1" y2="1">
          <stop offset="0" class="stop-white"/>
          <stop offset="1" class="stop-silver"/>
        </linearGradient>
        <linearGradient id="photo-kids" x1="0" y1="0" x2="0" y2="1">
          <stop offset="0" stop-color="#7fc4e6"/>
          <stop offset="1" stop-color="#2a7fc0"/>
        </linearGradient>
        <linearGradient id="photo-squad" x1="0" y1="0" x2="1" y2="1">
          <stop offset="0" stop-color="#b9c6d6"/>
          <stop offset="1" stop-color="#3a4a7a"/>
        </linearGradient>
        <linearGradient id="photo-meet" x1="0" y1="0" x2="0" y2="1">
          <stop offset="0" stop-color="#9fb6cc"/>
          <stop offset="1" stop-color="#2b8ccf"/>
        </linearGradient>
        <radialGradient id="photo-lane" cx="0.45" cy="0.4" r="0.7">
          <stop offset="0" stop-color="#6fd0f2"/>
          <stop offset="1" stop-color="#1877c0"/>
        </radialGradient>
      </defs>

      <rect class="back-base" width="840" height="560" fill="url(#back-navy)"/>

      <rect class="photo photo--squad" x="330" y="0" width="510" height="200" fill="url(#photo-squad)"
            role="img" aria-label="Photo of club swimmers in caps standing together on deck"/>
      <rect class="photo photo--meet" x="300" y="175" width="540" height="225" fill="url(#photo-meet)"
            role="img" aria-label="Photo of a swim meet with lanes, flags and starting blocks"/>
      <path class="photo-divider" d="M360 205 C500 168 690 158 840 176" fill="none" stroke="var(--white)" stroke-width="8"/>

      <path class="back-paper" d="M0 0 H385 Q350 95 285 150 L0 150 Z" fill="url(#back-paper)"/>
      <path class="photo photo--kids" d="M0 165 C90 128 200 118 292 126 L330 280 L0 280 Z" fill="url(#photo-kids)"
            role="img" aria-label="Photo of young swimmers in caps and goggles beside the pool"/>
      <path class="paper-edge" d="M385 0 Q350 95 285 150 Q150 130 0 165" fill="none" stroke="var(--white)" stroke-width="7"/>

      <g class="club-mark">
        <circle cx="62" cy="68" r="30" fill="var(--navy)"/>
        <text class="club-name club-name--dark" font-size="22">
          <tspan x="108" y="46">HARBOR</tspan>
          <tspan x="108" y="73">FINWAVE</tspan>
          <tspan x="108" y="100">CLUB</tspan>
        </text>
      </g>

      <path class="back-wave" d="M0 262 C140 236 290 226 410 262 C560 320 690 338 840 318 V560 H0 Z" fill="url(#back-navy)"/>

      <text class="quote" text-anchor="middle" font-size="17">
        <tspan x="220" y="292" font-size="21"><tspan class="quote-mark">❝</tspan>Harbor Finwave Club</tspan>
        <tspan x="220" y="316">is a Coach Run Swim Club, bringing</tspan>
        <tspan x="220" y="338">Passion &amp; Uniqueness to our</tspan>
        <tspan x="220" y="360">Athlete Centered Programs<tspan class="quote-mark">❞</tspan></tspan>
      </text>

      <g class="programs-ribbon">
        <path d="M72 384 H282 L272 396 L282 408 H72 L62 396 Z" fill="var(--orange)"/>
        <text class="ribbon-text" x="84" y="401">PROGRAMS WE OFFER ARE :-</text>
      </g>

      <g class="program-list">
        <rect class="bullet" x="40" y="426" width="5" height="5"/>
        <text x="52" y="432">Competitive Swim</text>
        <rect class="bullet" x="162" y="426" width="5" height="5"/>
        <text x="174" y="432">Swim Academy</text>
        <rect class="bullet" x="270" y="426" width="5" height="5"/>
        <text x="282" y="432">Fitness Swim</text>

        <rect class="bullet" x="40" y="446" width="5" height="5"/>
        <text x="52" y="452">Adult Swim &amp; Personal Training Programs (Online).</text>

        <rect class="bullet" x="40" y="466" width="5" height="5"/>
        <text x="52" y="472">We coach from High performance athletes to developmental.</text>

        <rect class="bullet" x="40" y="486" width="5" height="5"/>
        <text x="52" y="492">Highest Quality Coaching for Competitive Swim Swim Academy</text>
        <text x="52" y="510">(Comp &amp; Aquatic Leadership)</text>

        <rect class="bullet" x="40" y="524" width="5" height="5"/>
        <text x="52" y="530">Fitness Swim Online &amp; Private Programs (Upon request)</text>
      </g>

      <g class="contact-box">
        <rect x="470" y="440" width="370" height="120" fill="var(--ink)"/>
        <line x1="470" y1="440" x2="470" y2="560" stroke="var(--silver-dark)" stroke-width="2"/>
        <use href="#icon-phone" x="490" y="464" width="18" height="18" class="icon-accent"/>
        <text class="contact contact-phone" x="514" y="481" font-size="20">780-555-0147</text>
        <use href="#icon-mail" x="491" y="497" width="15" height="15" class="icon-accent"/>
        <text class="contact contact-line" x="514" y="509" font-size="13">coach@finwaveclub.com</text>
        <use href="#icon-globe" x="491" y="521" width="15" height="15" class="icon-accent" color="var(--orange)"/>
        <text class="contact contact-line" x="514" y="533" font-size="13">www.finwaveclub.com</text>
      </g>

      <g class="lane-badge">
        <circle cx="762" cy="395" r="72" fill="var(--navy)"/>
        <circle cx="762" cy="395" r="64" fill="var(--white)"/>
        <circle cx="762" cy="395" r="58" fill="url(#photo-lane)"
                role="img" aria-label="Photo of a swimmer in the water at the lane rope"/>
      </g>
    </svg>
  </section>

</main>
</body>
</html>
```